Open Horizon Circle - invitation / brochure

​​I am in need of a bi-fold invitation/brochure for an educational series called "Open Horizon Circle". This dinner series provides education and community for "Women in Transition" these are women who are currently getting divorced, recently divorced, or widowed.

I am a partner of a wealth management boutique that advises a small number of high-net-worth families. Additionally, I am married to one of the most prominent family law attorneys in the country. The combination of these two unique perspectives has allowed me to see there is an unfortunate dearth of impactful, powerful, and useful resources to help wealthy women transition from being married to being single. (via divorce and/or death of their spouse)

What, How & WHY I do my job:
As a wealth manager, the "what" and "how" aspects of my job are not materially different from most of my competitors. However, the thing that makes me completely unique, and without competition, is "why" I do my job.

I do this because so many women experience unwelcome and unproductive feelings when the dilution of their marriage is complete AND because there is virtually no good place for them to obtain the important information they truly need to move forward and lead a happy, full, prosperous, productive, and fun life. In the absence of this information, many women experience unwelcome, unpleasant, and unproductive emotions.

For example, some experience shame or fear that they have failed. Others struggle with the belief they wasted a significant portion of their life. Some struggle with unresolved anger over the entire experience. It's very difficult to process and work through these emotions by yourself and it can be hard to get the support and guidance they need from their best friends (most are not trained in this area) may well be married (functional or otherwise) and they often times don't have the times to be there when the newly divorced or widowed women need them most.

Usually, these negative feelings are most intense when they are looking backward in time. However, I have seen women go on and lead remarkably impressive lives. Lives that are ​more ​full, richer, more fun, dynamic, and rewarding than they expected possible.

More about the WHY I do what I do - I created Open Horizon Circle so women in transition have a safe, supportive and comfortable space for these women to support each other. While each woman's story is unique, the emotional consequences are fairly common and they do not need to feel alone as they process the sometimes difficult, conflicting, and unpredictable emotions.

I want them to connect with each other because they have a great appreciation and empathy for what all the other women are experiencing. A bi-product of attending and participating in the dinner is to forge friendships and connections with the other woman in attendance so they can be resources to each other when they need help dealing with their own fear, anxiety, or anger. IMPORTANT NOTE - THIS IS NOT A THERAPY OR SUPPORT GROUP. Instead, this is a select group of very successful and accomplished women who have a shared experience and while each is navigating their own path, they have an opportunity to learn important information, in a safe place, where they can share their experience, strength, and hope with each other.

I want the invitation/brochure to feel very bespoke, thoughtfully curated, and specifically designed to address the most important and impactful areas of life, health, and wellness. I want the invitation/brochure to communicate that the presenters are the best in class and thought leaders in their respective areas of expertise. I also want to communicate that they have so much to be excited about. Because they have substantial financial resources, they have a unique opportunity to reinvent themselves and lead a life beyond their wildest dreams. I hope they can see how and why they can stop feeling the negative feelings of anger, sadness, fear, guilt, remorse, and regret. My goal is to get them to look forward (as opposed to backward where the negative emotions come from) so they can be optimistic, excited, happy, joyful, and enthusiastic because they get to be whoever they want; live wherever and however they want. They are not defined nor controlled by their past. They have full control and abundant resources at their disposal to be happier and more fulfilled than they ever hoped or imagined.

The feelings of optimism, excitement, energetic, and joyfulness are very important to the messaging of the Open Horizon Circle. I'd like this to be a consistent theme throughout the invitation/brochure. Basically moving from a dark, sad, and negative past to a bright, fun, optimistic, rewarding, fulfilling, and dynamic future.

To create an exciting, rewarding and vibrant life they will want to (in some cases need to) learn new information and skills from the leading authorities in the most important and impactful areas of life.

The presenters at each dinner will focus on one of the "8 Dimensions of Wellness" so they can make thoughtful and informed decisions without fear, anxiety, and stress.

If you think of marriage as two people sailing a ship or flying a plane, the husband and wife often divide the responsibilities of running their affairs because it's too much for one person to manage all by themselves; besides they have a spouse who can help and often times they have different expertise. For illustration purposes, let's say the husband manages the even-numbered items and the wife manages the odd number of items. Each manages half but together everything is well managed and nothing falls through the cracks.

Post-divorce, the husband and wife now each have their own boat to sail and are responsible for all the items (odd and even-numbered) of their ship.

Unfortunately, these women are having to manage items that she has little to no experience with the even-numbered items the husband used to manage during the marriage. They have to take sole control of complicated matters that have serious and long-lasting consequences. That's great if they do a good job. However, given the scope, scale, and complexity of 7-10 figure net worth chances are they won't have the experience, expertise, intellectual resources, and time to manage all the even and odd numbers optimally.

The format of the Open Horizon Circle events will be an intimate dinner conversation, in a private room, at a 5 star restaurant in Chicago. There will be a thoughtfully curated group of 4-10 women at one round table to facilitate an interesting and informative presentation. It will be specifically curated for them and delivered. There is no cost to attend the event and they are welcome to attend as many as they like. I will be covering all the expenses related to dinner, drinks, valet parking, and the speaker or presenter.

Each monthly dinner will focus on 1 of the 8 Dimensions of Wellness:

1. Physical - Physical Activity, Good Nutrition, Sleep, Preventing Illness & Injury, and Managing Chronic Health Conditions.

2. Emotional - Coping Effectively with life and creating satisfying relationships.

3. Social - Developing a sense of connection, belonging, and a well-developed support system.

4. Intellectual - Recognizing one’s creative abilities and finding ways to expand knowledge and skills. Boost cognitive function, stimulate the brain, and fuel learning.

5. Environmental - Occupying pleasant, stimulating environments that support well-being.

6. Spiritual - Expanding a sense of purpose and meaning in life, including one’s morals and ethics. (May or may not involve religious activities). Meditation

7. Vocational - Gaining personal satisfaction and enrichment from one's work (maybe academic or professional). Share your talents, wisdom, and experience.

8. Financial - Satisfaction with current and future financial situations.

I'd like the invitation/brochure to give a general overview of the 8 dimensions of wellness and that each gathering will focus on one of the eight. The presentation will be done by women (some of whom went through a divorce or the death of a spouse) who are widely recognized as experts in their respective fields. The female presenters will be highly qualified and credentialed in their field - this could mean they are MDs or PhDs and/or have decades of experience in their specific area of expertise.

I'd like the invitation to be "timeless" meaning that it doesn't have specific dates, times, or locations included. However, if someone would like more information and details they can call or email me for the specific details of the next couple of dates, topics, locations, and menus. I am also open to having a QR code available on the brochure for them to contact me for additional information. Once they contact my office they will receive I will receive all the detailed information via a PDF so they can RSVP if they would like to attend. My goal is that I don't want the invitation/brochure to expire even though the event details change every month.

I will market the Open Horizon Circle program by distributing the invitation/brochures available via therapists, divorce lawyers, and grief counselors that specialize in this demographic of women in transition. They in turn will share the invitation/brochure with their woman in transition clients if they think they would benefit from the program

The look and feel I am going for with the brochure/invitation is high-end, contemporary, carefully curated content for a very special and specific community of high-net-worth women in transition that has the resources to be and do anything they want.

Vellora
Marlowe Crest
Duvaine
Kestrel Onyx Card
Shopping in Paris and London
Flying private
Vacationing in the Riviera & Monaco.
Beautiful people
Multi-generational - kids and grandkids.

The theme, feel, and messaging of the invitation/brochure should be consistent with the concept of moving away from – sadness, fear, regret, failure, and negative. And moving towards – joyful, happy, optimistic, exciting, successful, energetic, and contentment.

This information is intended to be informative, empowering, uplifting, transformational, and helpful - so they can lead a life that is bigger, brighter, and better than they ever dreamed of experiencing.

Target Market(s)

Wealthy woman who are currently getting divorced, recently divorced, or widowed. Generally the women will be mid-fourties and older..

Industry/Entity Type

Financial Services targeting wealthy windows and divorced woman.

Font styles to use
Serif
Sans Serif

Requirements
Must have
• The look and feel I am going for with the brochure/invitation is high-end, contemporary, carefully curated content for a very special and specific community of high-net-worth women in transition that has the resources to be and do anything they want. PLEASE ENSURE 70% OF THE WOMAN IN THE INVITATAION/BROCHURE OF NON-WHITE RACES & ETHNICITIES. The theme, feel, and messaging of the invitation/brochure should be consistent with the concept of moving away from – sadness, fear, regret, failure, and negative. And moving towards – joyful, happy, optimistic, exciting, successful, energetic, and contentment. This information is intended to be informative, empowering, uplifting, transformational, and helpful - so they can lead a life that is bigger, brighter, and better than they ever dreamed of experiencing.

```html
<!DOCTYPE html>
<html lang="en">
<head>
<meta charset="utf-8">
<title>Open Horizon Circle – Invitation Brochure</title>
<link rel="stylesheet" href="https://fonts.googleapis.com/css2?family=Cormorant+Garamond:wght@400;500;600&family=Great+Vibes&family=Open+Sans:wght@400;600&display=swap">
<style>
:root{
  --board:#4a4244;
  --cream:#f4ede5;
  --cream-warm:#f3e4d9;
  --mauve:#6e3c4a;
  --mauve-soft:#7a4552;
  --taupe:#a68d87;
  --linen:#e8ddd3;
  --peach:#c99a80;
  --rust:#b85a3a;
  --ink:#2e2628;
  --white:#ffffff;
}
*{margin:0;padding:0;box-sizing:border-box}
html,body{width:1200px;height:2935px;overflow:hidden;background:var(--board)}
body{position:relative;font-family:"Open Sans",Arial,sans-serif;color:var(--ink)}
.page{position:absolute;left:349px;width:519px;background:var(--cream);overflow:hidden}
.abs{position:absolute}
.photo{position:absolute}

/* cover */
.cover{top:56px;height:669px}
.cover-photo{left:0;top:0;width:519px;height:509px;
  background:
    radial-gradient(ellipse 90px 70px at 80px 170px,rgba(255,236,170,.95),rgba(255,210,130,0) 100%),
    radial-gradient(ellipse 70px 190px at 400px 200px,rgba(110,80,62,.75),rgba(110,80,62,0) 100%),
    radial-gradient(ellipse 150px 190px at 260px 300px,rgba(196,150,112,.8),rgba(196,150,112,0) 100%),
    radial-gradient(ellipse 110px 140px at 310px 250px,rgba(230,190,160,.7),rgba(230,190,160,0) 100%),
    linear-gradient(180deg,#a8925e 0%,#c9a060 18%,#d6a468 30%,#b48a6e 42%,#c9ad94 58%,#e6dacb 78%,#f1ebe2 100%)}
.cover-band{left:0;top:509px;width:519px;height:133px;
  background:linear-gradient(90deg,#c8957c 0%,#a86f6c 50%,#7a4552 100%)}
.cover-script{position:absolute;left:40px;right:0;top:4px;text-align:center;
  font-family:"Great Vibes",cursive;font-size:66px;color:var(--cream);line-height:1}
.cover-caps{position:absolute;left:66px;right:0;top:64px;text-align:center;
  font-family:"Cormorant Garamond",Georgia,serif;font-size:62px;letter-spacing:18px;color:var(--cream);line-height:1}
.cover-strip{left:0;top:642px;width:519px;height:18px;background:var(--cream-warm)}
.cover-base{left:0;top:660px;width:519px;height:9px;background:var(--mauve-soft)}

/* vision */
.vision{top:768px;height:678px}
.vision-photo{left:17px;top:12px;width:301px;height:206px;
  background:
    radial-gradient(ellipse 70px 60px at 235px 70px,rgba(255,246,200,1),rgba(255,220,120,0) 100%),
    radial-gradient(ellipse 80px 110px at 140px 110px,rgba(214,150,110,.85),rgba(214,150,110,0) 100%),
    radial-gradient(ellipse 70px 120px at 90px 120px,rgba(150,80,50,.75),rgba(150,80,50,0) 100%),
    linear-gradient(180deg,#d89a52 0%,#eab55e 45%,#b7953e 75%,#6f7a35 100%)}
.vision-intro{left:318px;top:12px;width:201px;height:206px;background:var(--mauve);
  color:var(--white);font-size:8.6px;line-height:11.3px;text-align:center;padding:27px 16px 0}
.vision-label{left:17px;top:218px;width:301px;height:32px;background:var(--rust);
  color:var(--cream);font-family:"Cormorant Garamond",Georgia,serif;font-size:23px;letter-spacing:5px;text-align:center;line-height:32px}
.vision-body{left:22px;top:268px;width:475px;font-size:9.2px;line-height:11.3px;text-align:justify}
.vision-note{left:22px;top:359px;width:475px;font-size:9.2px;line-height:11.3px;text-align:justify}
.vision-note strong{color:var(--rust);font-weight:600}
.dinner{left:17px;top:424px;width:301px;height:235px;
  background:linear-gradient(180deg,#c99a80 0%,#9b6669 35%,#6e3c4a 100%)}
.dinner-title{position:absolute;left:17px;top:22px;width:264px;height:62px;background:var(--mauve);
  color:var(--cream);text-align:center;font-family:"Cormorant Garamond",Georgia,serif;font-size:17px;line-height:18px;padding-top:6px}
.dinner-title .stars{font-size:12px;letter-spacing:3px;line-height:14px}
.dinner-text{position:absolute;left:17px;top:102px;width:264px;color:var(--cream);font-size:8.8px;line-height:11.3px;text-align:justify}
.dinner-photo{left:318px;top:424px;width:201px;height:235px;
  background:
    radial-gradient(circle 34px at 40px 40px,rgba(226,150,160,.9),rgba(226,150,160,0) 100%),
    radial-gradient(circle 30px at 150px 35px,rgba(232,170,170,.85),rgba(232,170,170,0) 100%),
    radial-gradient(ellipse 50px 25px at 60px 75px,rgba(120,150,100,.6),rgba(120,150,100,0) 100%),
    radial-gradient(ellipse 90px 40px at 80px 190px,rgba(255,255,255,.95),rgba(255,255,255,0) 100%),
    radial-gradient(ellipse 40px 50px at 170px 180px,rgba(196,160,100,.7),rgba(196,160,100,0) 100%),
    linear-gradient(180deg,#e9e2d8 0%,#f6f2ec 45%,#dcd2c2 100%)}
.vision-strip{left:0;top:667px;width:519px;height:11px;background:linear-gradient(90deg,var(--peach),var(--cream-warm))}

/* wellness */
.wellness{top:1489px;height:678px}
.dim{position:absolute;width:152px;height:196px;background:var(--linen)}
.dim-head{position:absolute;left:0;top:0;width:152px;height:120px;background:var(--taupe)}
.dim-pic{position:absolute;left:34px;top:8px;width:84px;height:84px;border-radius:50%;border:3px solid var(--white);overflow:hidden}
.dim-name{position:absolute;left:0;right:0;top:96px;text-align:center;
  font-family:"Cormorant Garamond",Georgia,serif;font-size:17px;letter-spacing:.5px;color:var(--cream)}
.dim-text{position:absolute;left:8px;right:8px;top:128px;text-align:center;font-size:8.4px;line-height:10.8px}
.dim-center{background:var(--mauve);text-align:center;color:var(--cream)}
.dim-eight{position:absolute;left:0;right:0;top:0;font-family:"Great Vibes",cursive;font-size:124px;line-height:1}
.dim-caption{position:absolute;left:0;right:0;top:120px;font-family:"Cormorant Garamond",Georgia,serif;font-size:19px;line-height:21px}
.dim-sub{position:absolute;left:0;right:0;top:170px;font-size:9px;font-style:italic}
.wellness-note{left:17px;top:626px;width:485px;height:32px;background:var(--rust);color:var(--cream);
  font-size:9px;line-height:11px;text-align:center;padding-top:5px}
.wellness-strip{left:0;top:668px;width:519px;height:10px;background:linear-gradient(90deg,var(--peach),var(--cream-warm))}

/* ship */
.ship{top:2210px;height:694px}
.ship-photo{left:0;top:0;width:268px;height:346px;
  background:
    radial-gradient(ellipse 45px 110px at 70px 170px,rgba(248,248,250,.95),rgba(248,248,250,0) 100%),
    radial-gradient(ellipse 160px 40px at 150px 320px,rgba(236,238,242,.95),rgba(236,238,242,0) 100%),
    linear-gradient(180deg,#5f8fc4 0%,#8fb4da 35%,#c8d8e8 55%,#3a6590 60%,#2f5a86 78%,#c9d0d8 92%,#e9ecef 100%)}
.ship-story{left:268px;top:0;width:251px;height:346px;
  background:linear-gradient(180deg,#c99a80 0%,#9b6669 50%,#6e3c4a 100%);
  color:var(--white);font-size:8.6px;line-height:11px;text-align:justify;padding:17px 14px 0 18px}
.ship-story p+p{margin-top:8px}
.ship-gallery{left:0;top:346px;width:519px;height:164px;background:var(--cream-warm)}
.ship-frame{position:absolute;left:14px;top:15px;width:491px;height:136px;border:1px solid var(--peach)}
.ship-jet{left:26px;top:370px;width:240px;height:118px;
  background:
    radial-gradient(ellipse 30px 55px at 90px 60px,rgba(205,180,150,.9),rgba(205,180,150,0) 100%),
    radial-gradient(ellipse 140px 22px at 150px 75px,rgba(250,250,250,.95),rgba(250,250,250,0) 100%),
    linear-gradient(180deg,#f1f0ee 0%,#e2e0dc 55%,#a9a49e 75%,#8f8a84 100%)}
.ship-city{left:266px;top:370px;width:234px;height:118px;
  background:
    radial-gradient(ellipse 40px 60px at 110px 80px,rgba(110,40,60,.95),rgba(110,40,60,0) 100%),
    radial-gradient(ellipse 25px 30px at 190px 95px,rgba(90,140,200,.85),rgba(90,140,200,0) 100%),
    radial-gradient(ellipse 25px 30px at 40px 100px,rgba(210,110,120,.8),rgba(210,110,120,0) 100%),
    linear-gradient(180deg,#f4f2ee 0%,#e4ded4 50%,#b7aea4 100%)}
.contact{left:0;top:510px;width:519px;height:130px;
  background:linear-gradient(100deg,#7a4552 0%,#a86f6c 55%,#c99a80 100%);
  color:var(--cream);text-align:center;font-family:"Cormorant Garamond",Georgia,serif;font-size:20px;letter-spacing:6px;line-height:130px}
.ship-strip{left:0;top:640px;width:519px;height:22px;background:var(--cream-warm)}
.ship-base{left:0;top:662px;width:519px;height:32px;background:var(--mauve-soft)}
</style>
</head>
<body>

<section class="page cover">
  <div class="photo cover-photo" role="img" aria-label="Smiling woman with wavy hair blended over a seaside swing at sunset"></div>
  <div class="abs cover-band">
    <div class="cover-script">Open Horizon</div>
    <div class="cover-caps">CIRCLE</div>
  </div>
  <div class="abs cover-strip"></div>
  <div class="abs cover-base"></div>
</section>

<section class="page vision">
  <div class="photo vision-photo" role="img" aria-label="Woman with eyes closed enjoying golden sunlight in a field"></div>
  <div class="abs vision-intro">I am a partner of a wealth management boutique that advises a small number of high-net-worth families. Additionally, I am married to one of the most prominent family law attorneys in the country. The combination of these two unique perspectives has allowed me to see there is an unfortunate dearth of impactful, powerful, and useful resources to help wealthy women transition from being married to being single. (via divorce and/or death of their spouse)</div>
  <div class="abs vision-label">OUR VISION</div>
  <p class="abs vision-body">I created Open Horizon Circle so women in transition have a safe, supportive and comfortable space for these women to support each other. While each woman's story is unique, the emotional consequences are fairly common and they do not need to feel alone as they process the sometimes difficult, conflicting, and unpredictable emotions. I want them to connect with each other because they have a great appreciation and empathy for what all the other women are experiencing. A bi-product of attending and participating in the dinner is to forge friendships and connections with the other woman in attendance so they can be resources to each other when they need help dealing with their own fear, anxiety, or anger.</p>
  <p class="abs vision-note"><strong>IMPORTANT NOTE - THIS IS NOT A THERAPY OR SUPPORT GROUP.</strong> Instead, this is a select group of very successful and accomplished women who have a shared experience and while each is navigating their own path, they have an opportunity to learn important information, in a safe place, where they can share their experience, strength, and hope with each other.</p>
  <div class="abs dinner">
    <div class="dinner-title"><div class="stars">★★★★★</div>INTIMATE DINNER<br>CONVERSATION</div>
    <p class="dinner-text">The format of the Open Horizon Circle events will be an intimate dinner conversation, in a private room, at a 5 star restaurant in Chicago. There will be a thoughtfully curated group of 4-10 women at one round table to facilitate an interesting and informative presentation. It will be specifically curated for them and delivered. There is no cost to attend the event and they are welcome to attend as many as they like. I will be covering all the expenses related to dinner, drinks, valet parking, and the speaker or presenter.</p>
  </div>
  <div class="photo dinner-photo" role="img" aria-label="Elegant round dinner tables with white linens and floral centerpieces"></div>
  <div class="abs vision-strip"></div>
</section>

<section class="page wellness">
  <div class="dim" style="left:17px;top:11px">
    <div class="dim-head"><div class="dim-pic" role="img" aria-label="Woman leaping in a dance pose" style="background:radial-gradient(ellipse 14px 30px at 45px 40px,#3f8c8a,rgba(63,140,138,0)),linear-gradient(90deg,#f3f4f2,#dfe4e2 60%,#f3f4f2)"></div><div class="dim-name">PHYSICAL</div></div>
    <p class="dim-text">Physical Activity, Good Nutrition, Sleep, Preventing Illness &amp; Injury, and Managing Chronic Health Conditions.</p>
  </div>
  <div class="dim" style="left:185px;top:11px">
    <div class="dim-head"><div class="dim-pic" role="img" aria-label="Joyful woman outdoors among greenery" style="background:radial-gradient(ellipse 20px 32px at 40px 44px,#e8dcc8,rgba(232,220,200,0)),linear-gradient(160deg,#8a8a5a,#c6a86a 50%,#6f7447)"></div><div class="dim-name">EMOTIONAL</div></div>
    <p class="dim-text">Coping Effectively with life and creating satisfying relationships</p>
  </div>
  <div class="dim" style="left:352px;top:11px">
    <div class="dim-head"><div class="dim-pic" role="img" aria-label="Group of laughing women friends" style="background:radial-gradient(circle 18px at 28px 30px,#6b4332,rgba(107,67,50,0)),radial-gradient(circle 18px at 56px 50px,#e0c09a,rgba(224,192,154,0)),linear-gradient(160deg,#c49a7a,#8a5a44)"></div><div class="dim-name">SOCIAL</div></div>
    <p class="dim-text">Developing a sense of connection, belonging, and a well-developed support system.</p>
  </div>
  <div class="dim" style="left:17px;top:217px">
    <div class="dim-head"><div class="dim-pic" role="img" aria-label="Woman painting at an easel outdoors" style="background:radial-gradient(ellipse 14px 30px at 34px 40px,#fbfbf8,rgba(251,251,248,0)),linear-gradient(180deg,#eef1f2 0%,#dfe6e4 45%,#7d9a5e 60%,#4f6e3a 100%)"></div><div class="dim-name">INTELLECTUAL</div></div>
    <p class="dim-text">Recognizing one's creative abilities &amp; finding ways to expand knowledge &amp; skills. Boost cognitive function, stimulate the brain and fuel learning.</p>
  </div>
  <div class="dim dim-center" style="left:185px;top:217px">
    <div class="dim-eight">8</div>
    <div class="dim-caption">DIMENSIONS<br>OF WELLNESS</div>
    <div class="dim-sub">(1 Topic / monthly dinner)</div>
  </div>
  <div class="dim" style="left:352px;top:217px">
    <div class="dim-head"><div class="dim-pic" role="img" aria-label="Colourful Riviera harbour town" style="background:linear-gradient(180deg,#9cbcd8 0%,#7a9a6a 28%,#d08a5a 42%,#e8c07a 52%,#c86a4a 60%,#2e9ab0 72%,#1f7f98 100%)"></div><div class="dim-name">ENVIRONMENTAL</div></div>
    <p class="dim-text">Occupying pleasant, stimulating environments that support well-being.</p>
  </div>
  <div class="dim" style="left:17px;top:424px">
    <div class="dim-head"><div class="dim-pic" role="img" aria-label="Woman meditating" style="background:radial-gradient(ellipse 22px 34px at 39px 46px,#6b4a38,rgba(107,74,56,0)),radial-gradient(ellipse 30px 14px at 39px 70px,#f4f1ec,rgba(244,241,236,0)),linear-gradient(180deg,#f3f3f1,#e4e1dc)"></div><div class="dim-name">SPIRITUAL</div></div>
    <p class="dim-text">Expanding a sense of purpose &amp; meaning in life, including one's morals and ethics. (May or may not involve religious activities). Meditation</p>
  </div>
  <div class="dim" style="left:185px;top:424px">
    <div class="dim-head"><div class="dim-pic" role="img" aria-label="Professional woman in a bright office" style="background:radial-gradient(ellipse 20px 34px at 40px 48px,#fafafa,rgba(250,250,250,0)),radial-gradient(ellipse 12px 14px at 40px 22px,#c9a27a,rgba(201,162,122,0)),linear-gradient(180deg,#eef0ea,#cfd4c4)"></div><div class="dim-name">VOCATIONAL</div></div>
    <p class="dim-text">Gaining personal satisfaction and enrichment from one's work (maybe academic or professional). Share your talents, wisdom &amp; experience.</p>
  </div>
  <div class="dim" style="left:352px;top:424px">
    <div class="dim-head"><div class="dim-pic" role="img" aria-label="Kestrel Onyx Card" style="background:var(--white)"><svg width="78" height="78" viewBox="0 0 78 78"><rect x="14" y="24" width="50" height="31" rx="3" fill="#1b1b1d"/></svg></div><div class="dim-name">FINANCIAL</div></div>
    <p class="dim-text">Satisfaction with current and future financial situations.</p>
  </div>
  <p class="abs wellness-note">The presentation will be done by women (some of whom went through a divorce or the death of<br>a spouse) who are widely recognized as experts in their respective fields.</p>
  <div class="abs wellness-strip"></div>
</section>

<section class="page ship">
  <div class="photo ship-photo" role="img" aria-label="Woman in white relaxing on the bow of a sailing yacht at sea"></div>
  <div class="abs ship-story">
    <p>If you think of marriage as two people sailing a ship or flying a plane, the husband and wife often divide the responsibilities of running their affairs because it's too much for one person to manage all by themselves; besides they have a spouse who can help and often times they have different expertise. For illustration purposes, let's say the husband manages the even-numbered items and the wife manages the odd number of items. Each manages half but together everything is well managed and nothing falls through the cracks. Post-divorce, the husband and wife now each have their own boat to sail and are responsible for all the items (odd and even-numbered) of their ship.</p>
    <p>Unfortunately, these women are having to manage items that she has little to no experience with the even-numbered items the husband used to manage during the marriage. They have to take sole control of complicated matters that have serious and long-lasting consequences. That's great if they do a good job. However, given the scope, scale, and complexity of 7-10 figure net worth chances are they won't have the experience, expertise, intellectual resources, and time to manage all the even and odd numbers optimally.</p>
  </div>
  <div class="abs ship-gallery"><div class="ship-frame"></div></div>
  <div class="photo ship-jet" role="img" aria-label="Woman walking beside a private jet on the tarmac"></div>
  <div class="photo ship-city" role="img" aria-label="Woman with shopping bags in a European city square"></div>
  <div class="abs contact">CONTACT US</div>
  <div class="abs ship-strip"></div>
  <div class="abs ship-base"></div>
</section>

</body>
</html>
```